Welcome Card Banner Desing for email suscriptors

to get involved on this task please check my site tuvelisora.app
I wish for this task a welcome postal card to get subscribers for the newsletter and get a Coupon Code for discounts,
Keep in mind Velisora is a platform where customers (girls) can get any fashion high-end accessories ready to wear, to see the categories please visit our shop.

Target Market(s)

World wide people between 18-60 years old

Industry/Entity Type

Fashion

Coding

Coded - Design and coding required

Number of Pages Required

1 page

Font styles to use
Sans Serif

Colors
a64599
ffffff
ffc214
faa54b

Requirements
Must have
• Simplicity
• to get involved on this task please check my site tuvelisora.app
• I wish for this task a welcome postal card to get subscribers for the newsletter and get a Coupon Code for discounts,
• Keep in mind Velisora is a platform where customers (girls) can get any fashion high-end accessories ready to wear, to see the categories please visit our shop.
Nice to have
• Field for customer fill an email or just skip the banner
Should not have
• Bad grammar

```html
<!DOCTYPE html>
<html lang="en">
<head>
<meta charset="utf-8">
<title>Velisora — Welcome Card</title>
<link rel="stylesheet" href="https://fonts.googleapis.com/css2?family=Arimo:wght@400;700&family=PT+Sans:wght@400&display=swap">
<style>
  :root {
    --page-bg: #efeeec;
    --white: #ffffff;
    --button-bg: #efeeec;
    --ink: #2d2a26;
    --discount-ink: rgba(196, 112, 36, 0.78);
    --paper-light: #d9b27a;
    --paper-mid: #c8965a;
    --paper-dark: #a8723c;
    --photo-warm: #c9582a;
    --photo-dark: #3b2f28;
    --photo-light: #b8b0a4;
    --dash: #3a3128;
  }
  * { margin: 0; padding: 0; box-sizing: border-box; }
  html, body {
    width: 1200px;
    height: 2486px;
    overflow: hidden;
    background: var(--page-bg);
  }
  body { position: relative; font-family: "Arimo", Arial, sans-serif; }

  .welcome-card {
    position: absolute;
    left: 98px;
    top: 68px;
    width: 1004px;
    height: 2254px;
  }

  .hero {
    position: absolute;
    left: 0; top: 0;
    width: 1004px;
    height: 746px;
    overflow: hidden;
  }
  .hero-photo {
    position: absolute;
    inset: 0;
    background:
      radial-gradient(ellipse 45% 55% at 68% 55%, var(--photo-warm) 0%, rgba(201,88,42,0.85) 45%, rgba(201,88,42,0) 75%),
      linear-gradient(180deg, var(--photo-light) 0%, #a69c90 55%, var(--photo-dark) 100%);
  }
  .hero-title {
    position: absolute;
    left: 0; right: 0;
    top: 150px;
    text-align: center;
    color: var(--white);
    font-weight: 700;
    font-size: 84px;
    line-height: 110px;
    letter-spacing: -1px;
    text-shadow: 3px 4px 4px rgba(0,0,0,0.55);
    padding-left: 0;
  }
  .hero-dot {
    position: absolute;
    left: 164px; top: 423px;
    width: 26px; height: 26px;
    border-radius: 50%;
    background: var(--white);
  }
  .subscribe-button {
    position: absolute;
    left: 129px; top: 529px;
    width: 742px; height: 101px;
    background: var(--button-bg);
    border: none;
    font-family: "Arimo", Arial, sans-serif;
    font-weight: 700;
    font-size: 41px;
    color: var(--ink);
    display: flex; align-items: center; justify-content: center;
  }

  .offer {
    position: absolute;
    left: 0; top: 746px;
    width: 1004px;
    height: 1508px;
    overflow: hidden;
  }
  .offer-paper {
    position: absolute;
    inset: 0;
    background:
      radial-gradient(ellipse 60% 40% at 50% 40%, var(--paper-light) 0%, rgba(217,178,122,0) 80%),
      radial-gradient(ellipse 70% 50% at 50% 90%, #d4a86c 0%, rgba(212,168,108,0) 80%),
      linear-gradient(180deg, var(--paper-mid) 0%, #cfa066 50%, var(--paper-dark) 100%);
  }
  .discount-title {
    position: absolute;
    left: 0; right: 0;
    top: 313px;
    text-align: center;
    font-size: 136px;
    font-weight: 400;
    color: var(--discount-ink);
    letter-spacing: -2px;
    line-height: 1;
  }
  .discount-amount {
    position: absolute;
    left: 0; right: 0;
    top: 474px;
    text-align: center;
    font-size: 92px;
    font-weight: 400;
    color: var(--ink);
    letter-spacing: -1px;
    line-height: 1;
  }
  .coupon-button {
    position: absolute;
    left: 154px; top: 825px;
    width: 691px; height: 101px;
    border: 2px dashed var(--dash);
    display: flex; align-items: center; justify-content: center;
    font-weight: 700;
    font-size: 51px;
    color: var(--white);
    text-shadow: 3px 3px 3px rgba(120,60,10,0.75);
  }
  .brand-name {
    position: absolute;
    left: 0; right: 0;
    top: 1315px;
    text-align: center;
    font-family: "Arimo", Arial, sans-serif;
    font-weight: 700;
    font-size: 44px;
    color: #1e1a17;
  }
  .copyright {
    position: absolute;
    left: 0; right: 0;
    top: 1398px;
    text-align: center;
    font-family: "PT Sans", Arial, sans-serif;
    font-size: 22px;
    color: #3a2f25;
  }
  .footer-dot {
    position: absolute;
    left: 477px; top: 1485px;
    width: 46px; height: 46px;
    border-radius: 50%;
    background: var(--white);
  }
</style>
</head>
<body>
  <main class="welcome-card">
    <section class="hero">
      <div class="hero-photo" role="img" aria-label="Photo of a woman in red glitter heels holding an orange leather handbag on a sofa"></div>
      <h1 class="hero-title">"Welcome<br>to the finest<br>shop"</h1>
      <span class="hero-dot"></span>
      <div class="subscribe-button">Subscribe</div>
    </section>

    <section class="offer">
      <div class="offer-paper" role="img" aria-label="Aged crumpled paper texture background"></div>
      <h2 class="discount-title">Discount</h2>
      <p class="discount-amount">Upto 30%</p>
      <div class="coupon-button">get coupon code</div>
      <p class="brand-name">Velisora</p>
      <p class="copyright">©Copyright 2019, Velisora</p>
      <span class="footer-dot"></span>
    </section>
  </main>
</body>
</html>
```